Easy Business Card / Presentation Cover Design Project

We are looking for a business card design, covers for powerpoint presentations for investors, and possibly simple stationary for a Chicago real estate development firm. Our new logo is attached below.

We rehab and provide newly constructed homes. We are not a real estate brokerage firm (i.e., agents such as Meridale 47) and only operate in the Chicago area.

In terms of design, sophisticated and high end that would appeal to investors (theme should resemble investment banks, hedge funds, private equity rather than tech startup).

Target Market(s)

Investors, banks, financing sources

Industry/Entity Type

Real Estate

Requirements
Must have
• Two deliverables here. 1) Business card 2) Covers for powerpoint presentation.

Must be able to look sophisticated and high end when printed. Please think through the type of printing that will be needed. Would prefer something that can be printed in raised ink but digital is ok as well.

Will be printed on heavy paper.

Business Card: Horizontal Layout, no black backgrounds,

For presentation front cover, should include logo only. For back cover, should include contact info. Horizontal and should not contain any information that will need to be changed (i.e. date or client name)
Nice to have
• Would like to have the edges colored but not required. Please show multiple designs
Should not have
• Should not have any die cut or embossed type of designs. Shape should be standard size.

We are not a design firm, a retail firm, or a consumer product firm.

Please do not incorporate a house, buildings, etc. This must be very professional looking.

```html
<!DOCTYPE html>
<html lang="en">
<head>
<meta charset="utf-8">
<title>Larkfield Homes — Business Card</title>
<link rel="stylesheet" href="https://fonts.googleapis.com/css2?family=Exo+2:wght@300;400&display=swap">
<style>
  :root {
    --backdrop: #e9e6e1;
    --card: #f7f7f7;
    --card-edge: #dcdcdc;
    --ink-grey: #6f7377;
    --ink-dark: #4c4f53;
    --ink-blue: #2f86d6;
    --shadow: rgba(60, 50, 40, 0.18);
  }
  html, body {
    margin: 0;
    padding: 0;
    width: 1200px;
    height: 900px;
    overflow: hidden;
    background: var(--backdrop);
  }
  .canvas {
    position: relative;
    width: 1200px;
    height: 900px;
    font-family: "Exo 2", sans-serif;
  }
  .card {
    position: absolute;
    top: 297px;
    width: 500px;
    height: 306px;
    background: linear-gradient(160deg, #ffffff 0%, var(--card) 60%, #efefef 100%);
    border: 1px solid var(--card-edge);
    box-shadow: 0 6px 18px var(--shadow);
    box-sizing: border-box;
  }
  .card--info { left: 70px; }
  .card--brand { left: 630px; }

  .wordmark {
    position: absolute;
    top: 38px;
    right: 40px;
    font-size: 22px;
    font-weight: 300;
    letter-spacing: 2px;
    line-height: 1.05;
    text-align: right;
    color: var(--ink-dark);
    text-transform: uppercase;
  }

  .contact-list {
    position: absolute;
    left: 40px;
    bottom: 40px;
    margin: 0;
    padding: 0;
    list-style: none;
    font-size: 15px;
    font-weight: 300;
    line-height: 1.55;
    white-space: nowrap;
  }
  .contact-list .label { color: var(--ink-grey); }
  .contact-list .value { color: var(--ink-blue); }

  .brand-lockup {
    position: absolute;
    inset: 0;
    display: flex;
    align-items: center;
    justify-content: center;
    gap: 18px;
  }
  .brand-lockup svg { display: block; }
  .brand-lockup .brand-name {
    font-size: 26px;
    font-weight: 300;
    letter-spacing: 3px;
    color: var(--ink-blue);
    text-transform: uppercase;
  }
</style>
</head>
<body>
<main class="canvas">
  <section class="card card--info" aria-label="Business card, contact side">
    <div class="wordmark">Larkfield<br>Homes</div>
    <ul class="contact-list">
      <li><span class="label">phone: </span><span class="value">312 555 0148</span></li>
      <li><span class="label">e-mail: </span><span class="value">hello@larkfieldhomes.com</span></li>
      <li><span class="label">address: </span><span class="value">1180 Wells Avenue Chicago IL 60607</span></li>
    </ul>
  </section>

  <section class="card card--brand" aria-label="Business card, brand side">
    <div class="brand-lockup">
      <svg width="44" height="44" viewBox="0 0 44 44" aria-hidden="true">
        <circle cx="22" cy="22" r="19" fill="none" stroke="var(--ink-blue)" stroke-width="3"/>
      </svg>
      <span class="brand-name">Larkfield Homes</span>
    </div>
  </section>
</main>
</body>
</html>
```